Boutique Shoe Bag Race wear Business Card Design

We are a new luxury shoe bag, jewellery and race wear store stocking local and international designers. Located in the fashion precinct of beautiful Marlow Cove famous in Sydney Australia. Stocking French jewellery and shoes such as Maximilien verdacs plus Australian made. Looking at quality and service and looking after the locals and tourists.
Ideas: White background, Black writing in bold engravers, logo in middle of Bondi and Boutique a gold horseshoe (facing upright so the curve is at the bottom) with a black stiletto inside. French clover silver and black border (not irish clover the French lattice type look)

Larkspur Parlour

I open 8/4 so require business card design ASAP.

Please place gold horseshoe facing upwards with the black stiletto inside.

Bold engravers writing for business name.

I will have my phone number tomorrow to update.

Border in similar/same style as attached picture with black/silver clover French design.

Thank you. Petra                                   

Industry/Entity Type

Fashion

Contact Information for Business Card

Larkspur Parlour
Boutique Owner Petra Halvorsen
41B Tindle Road
Marlow Cove NSW 2389 Australia
0491237406
02 **** *TBA
info@larkspurparlour.com.au
Facebook.com/LarkspurParlour
www.larkspurparlour.com.au

Font styles to use
Other font styles liked:
• Bold Engravers

Requirements
Must have
• Info on one side including business name and logo with black stiletto and gold horse shoe. reverse side with French clover border and Larger name Larkspur Parlour with logo in centre.
Should not have
• irish clover
French script
horseshoe upside down

```html
<!DOCTYPE html>
<html lang="en">
<head>
<meta charset="utf-8">
<title>Larkspur Parlour – Business Card</title>
<link rel="stylesheet" href="https://fonts.googleapis.com/css2?family=Cinzel:wght@700;900&family=Crimson+Pro:ital,wght@0,400;1,400&family=Open+Sans:wght@400&display=swap">
<style>
  :root {
    --backdrop: #151515;
    --card: #ffffff;
    --card-edge: #cfcfcf;
    --gold: #b3a333;
    --ink: #111111;
    --text: #454545;
    --rule: #c9c9c9;
    --border-band: linear-gradient(90deg, #ececec, #dedede 50%, #ececec);
    --label: #ffffff;
  }
  * { box-sizing: border-box; margin: 0; padding: 0; }
  html, body {
    width: 895px;
    height: 1200px;
    overflow: hidden;
    background: var(--backdrop);
  }
  .sheet { position: relative; width: 895px; height: 1200px; }

  .card {
    position: absolute;
    left: 41px;
    width: 817px;
    height: 505px;
    background: var(--card);
    border: 1px solid var(--card-edge);
  }
  .card--front { top: 43px; }
  .card--back { top: 622px; }

  .side-label {
    position: absolute;
    left: 41px;
    font-family: "Open Sans", Arial, sans-serif;
    font-size: 15px;
    color: var(--label);
  }
  .side-label--front { top: 555px; }
  .side-label--back { top: 1134px; }

  /* Front */
  .brand-mark {
    position: absolute;
    top: 66px;
    left: 0;
    width: 100%;
    text-align: center;
    font-family: "Cinzel", "Times New Roman", serif;
    font-weight: 700;
    font-size: 20px;
    letter-spacing: 3px;
    color: var(--gold);
  }
  .owner-name {
    position: absolute;
    top: 154px;
    left: 0;
    width: 100%;
    text-align: center;
    font-family: "Cinzel", "Times New Roman", serif;
    font-weight: 700;
    font-size: 47px;
    letter-spacing: 0.5px;
    color: var(--gold);
    line-height: 1;
  }
  .name-rule {
    position: absolute;
    top: 210px;
    left: 189px;
    width: 447px;
    height: 1px;
    background: var(--rule);
  }
  .owner-title {
    position: absolute;
    top: 213px;
    left: 0;
    width: 100%;
    text-align: center;
    font-family: "Crimson Pro", Georgia, serif;
    font-style: italic;
    font-size: 19px;
    letter-spacing: 1.6px;
    color: var(--text);
  }
  .contact {
    position: absolute;
    top: 274px;
    font-family: "Crimson Pro", Georgia, serif;
    font-size: 19px;
    line-height: 24.5px;
    letter-spacing: 1px;
    color: var(--text);
    font-style: normal;
  }
  .contact--address { right: 408px; text-align: right; }
  .contact--online { left: 438px; letter-spacing: 0.6px; }

  .border-band {
    position: absolute;
    height: 43px;
    background: var(--border-band);
  }
  .card--front .border-band { top: 429px; left: 31px; width: 755px; }
  .card--back .border-band { left: 34px; width: 758px; }
  .card--back .border-band--top { top: 31px; }
  .card--back .border-band--bottom { top: 430px; }

  /* Back */
  .brand-name {
    position: absolute;
    top: 234px;
    left: 0;
    width: 100%;
    text-align: center;
    font-family: "Cinzel", "Times New Roman", serif;
    font-weight: 900;
    font-size: 36px;
    letter-spacing: 7px;
    color: var(--ink);
    line-height: 1;
  }
</style>
</head>
<body>
<main class="sheet">

  <section class="card card--front" aria-label="Front side">
    <div class="brand-mark">Larkspur Parlour</div>
    <h1 class="owner-name">Petra Halvorsen</h1>
    <div class="name-rule"></div>
    <p class="owner-title">Larkspur Parlour Boutique Owner</p>
    <address class="contact contact--address">
      41B Tindle Road Marlow Cove<br>
      NSW 2389 Australia<br>
      0491237406<br>
      02 **** *TBA
    </address>
    <p class="contact contact--online">
      info@larkspurparlour.com.au<br>
      Facebook.com/LarkspurParlour<br>
      www.larkspurparlour.com.au
    </p>
    <div class="border-band" role="img" aria-label="Decorative border of clover motifs in diamond frames"></div>
  </section>
  <p class="side-label side-label--front">Front side</p>

  <section class="card card--back" aria-label="Back side">
    <div class="border-band border-band--top" role="img" aria-label="Decorative border of clover motifs in diamond frames"></div>
    <h2 class="brand-name">Larkspur Parlour</h2>
    <div class="border-band border-band--bottom" role="img" aria-label="Decorative border of clover motifs in diamond frames"></div>
  </section>
  <p class="side-label side-label--back">Back side</p>

</main>
</body>
</html>
```